New Fiction Writer Needs Visually Stunning eBook Cover Design

First time author needs a cover design for an ebook titled "Velvet Lanterns". The book is fiction and follows a smalltown southern teenage girl who loves to dance and dreams of world travel (particularly Paris & the Marlowe Spire) as she moves to Los Angeles and her life takes an unexpected romantic turn. Her grandmother, who has a few secrets, is an important person in her life. It is often hard for our protagonist to tell who the "good guys" are from the "bad guys".

A concept idea would be a young woman with one foot in a small town and the other in a big city. Other backdrops that might make for a good cover are fireworks, a young woman/women dancing (ballet or rockettes type), the Marlowe Spire or a young woman in a very bright, colorful 50s style dress with red shoes.

Any color scheme will work as long as the look will appeal to primarily female readers 18-45 (so somewhere between young/edgy and elegant). I need something that's going to make people want to give this book a chance when they haven't heard of the author.

Cover size is 6 in. x 9 in.

The author is Margaret Holloway
Updates

I want to thank everyone who submitted designs for all of your hard work on this project, the multiple redesigns and working with my feedback.  It was not an easy decision - there were so many wonderful designs- and different people loved different designs.  Unfortunately, I could only choose one.  I will certainly be telling people about the wonderful designers on PixelGuild and I wish you all the best.

Target Market(s)

Young women between about 15-45, romance/drama/mystery readers

Industry/Entity Type

Travel

Requirements
Must have
• Must Have:
When the artwork is generated, the files we would like to receive are:
The original working file PSD (Pictoria Document)
All the working elements including: illustrations, photos, graphics and fonts
A high resolution (300 dpi), 8.5 x 11 (o- Once r larger) file
A JPG file in the exact size specifications and color required by our publisher
A JPG file in the exact size for online POD or ebook (Quillo requires 900x600 and Fabl requires the short side to be at least 750)
A JPG black and white (gray scale) variation

```html
<!DOCTYPE html>
<html lang="en">
<head>
<meta charset="utf-8">
<title>Velvet Lanterns — Full Cover Wrap</title>
<link rel="stylesheet" href="https://fonts.googleapis.com/css2?family=Cinzel:wght@400;600&family=Open+Sans:wght@400&display=swap">
<style>
  :root {
    --page: #ffffff;
    --wine-deep: #2a0d0c;
    --wine-dark: #3e1513;
    --wine: #6e2a26;
    --rose: #a8544c;
    --rose-light: #c98a80;
    --silver-hi: #ffffff;
    --silver: #cfd3d6;
    --silver-lo: #7d8287;
    --body-text: #f4eae8;
  }
  * { margin: 0; padding: 0; box-sizing: border-box; }
  html, body {
    width: 1200px; height: 720px; overflow: hidden;
    background: var(--page);
  }
  .cover-wrap {
    position: absolute; left: 170px; top: 0;
    width: 1030px; height: 720px;
    display: flex;
  }
  .back-cover {
    position: relative; width: 478px; height: 100%;
    background:
      radial-gradient(ellipse at 40% 35%, var(--wine) 0%, var(--wine-dark) 55%, var(--wine-deep) 100%);
  }
  .back-blurb {
    position: absolute; left: 88px; top: 62px; width: 330px;
    font-family: "Open Sans", Arial, sans-serif;
    font-size: 10.5px; line-height: 21px;
    color: var(--body-text);
  }
  .back-blurb p + p { margin-top: 21px; }
  .spine {
    position: relative; width: 90px; height: 100%;
    background: linear-gradient(90deg, var(--wine-deep), var(--wine-dark) 40%, var(--wine-deep));
  }
  .spine-text {
    position: absolute; left: 8px; top: 36px;
    writing-mode: vertical-rl;
    display: flex; align-items: baseline; gap: 44px;
    font-family: "Cinzel", "Times New Roman", serif;
    color: var(--silver);
  }
  .spine-author { font-size: 26px; letter-spacing: 1px; }
  .spine-title { font-size: 54px; letter-spacing: 1px; }
  .front-cover {
    position: relative; flex: 1; height: 100%;
    background:
      radial-gradient(ellipse at 45% 62%, var(--rose) 0%, var(--wine) 35%, transparent 65%),
      radial-gradient(ellipse at 55% 22%, var(--rose-light) 0%, var(--rose) 25%, var(--wine) 55%, var(--wine-deep) 100%);
  }
  .front-title, .front-author {
    position: absolute; left: 0; right: 0; text-align: center;
    font-family: "Cinzel", "Times New Roman", serif;
    background: linear-gradient(180deg, var(--silver-hi) 0%, var(--silver) 45%, var(--silver-lo) 55%, var(--silver) 80%, var(--silver-hi) 100%);
    -webkit-background-clip: text; background-clip: text;
    color: transparent;
    filter: drop-shadow(1px 2px 2px rgba(0,0,0,0.7));
  }
  .front-title { top: 430px; line-height: 92px; font-weight: 400; }
  .title-line { display: block; font-size: 70px; letter-spacing: 2px; }
  .title-line .initial { font-size: 92px; }
  .front-author { top: 630px; font-size: 28px; letter-spacing: 1px; }
  .front-author .initial { font-size: 36px; }
</style>
</head>
<body>
  <main class="cover-wrap">
    <section class="back-cover" role="img" aria-label="Dark wine-red damask textured backdrop">
      <div class="back-blurb">
        <p>Lila Mae Turner has spent seventeen summers dancing barefoot on her grandmother's porch, dreaming of Paris and the lights of the Marlowe Spire. When a scholarship carries her west to Los Angeles, she packs her red shoes and a head full of plans.</p>
        <p>The city moves faster than any music she knows. New friends smile too easily, and the boy who catches her eye at rehearsal seems to know more about her family than she does.</p>
        <p>Back home, her grandmother guards letters she has never shown anyone. As the past begins to unfold, Lila must decide whom to trust before the last dance ends.</p>
        <p>A tender, twisting story of first love, family secrets and the courage to step onto a bigger stage.</p>
      </div>
    </section>

    <section class="spine">
      <div class="spine-text">
        <span class="spine-author">Margaret Holloway</span>
        <span class="spine-title">VELVET LANTERNS</span>
      </div>
    </section>

    <section class="front-cover" role="img" aria-label="Close-up photograph of worn red satin ballet slippers with ribbons and laces">
      <h1 class="front-title">
        <span class="title-line"><span class="initial">V</span>ELVET</span>
        <span class="title-line"><span class="initial">L</span>ANTERNS</span>
      </h1>
      <p class="front-author"><span class="initial">M</span>ARGARET <span class="initial">H</span>OLLOWAY</p>
    </section>
  </main>
</body>
</html>
```